We need visit card and a letter paper for our website. thx

We have a beauty clinic in Switzerland.
https://wolkenbachtal.ch
We need a visit card.

Requirements
Must have
• see colors on website

```html
<!DOCTYPE html>
<html lang="de">
<head>
<meta charset="utf-8">
<title>Wolkenbachtal – Visitenkarte</title>
<link rel="stylesheet" href="https://fonts.googleapis.com/css2?family=Lato:wght@400;700;900&display=swap">
<style>
  :root {
    --page-bg: #3b3b3d;
    --card-bg: #232224;
    --ink: #ffffff;
    --ink-soft: #e6e6e6;
    --accent: #d2467f;
    --rule: #d8d8d8;
  }
  * { box-sizing: border-box; margin: 0; padding: 0; }
  html, body {
    width: 1200px; height: 970px; overflow: hidden;
    background: var(--page-bg);
    font-family: "Lato", sans-serif;
    color: var(--ink);
  }
  .sheet {
    position: relative; width: 1200px; height: 970px;
    display: flex; flex-direction: column; align-items: center; justify-content: center;
    gap: 50px;
  }
  .card {
    position: relative;
    width: 720px; height: 410px;
    background: var(--card-bg);
    box-shadow: 0 12px 30px rgba(0,0,0,.45);
    overflow: hidden;
  }
  .card__band {
    position: absolute; left: 0; right: 0; bottom: 0;
    height: 9px; background: var(--accent);
  }

  /* brand name (plain text in place of the mark) */
  .brand-name {
    position: absolute;
    font-weight: 400; color: var(--ink);
    line-height: 1; text-align: center; white-space: nowrap;
  }
  .card--front .brand-name { left: 0; right: 0; top: 140px; font-size: 60px; }
  .card--back .brand-name { left: 20px; width: 345px; top: 175px; font-size: 38px; }

  .front__url {
    position: absolute; left: 0; right: 0; bottom: 58px;
    text-align: center; font-size: 17px; font-weight: 400;
    letter-spacing: 6px; color: var(--ink-soft);
  }

  /* back */
  .back__divider {
    position: absolute; left: 385px; top: 95px; width: 1.5px; height: 210px;
    background: var(--rule);
  }
  .contact {
    position: absolute; left: 420px; top: 92px; width: 290px;
  }
  .contact__name { font-size: 30px; font-weight: 900; line-height: 1.1; }
  .contact__role { font-size: 17px; font-weight: 400; margin-top: 4px; color: var(--ink-soft); }
  .contact__address { font-size: 17px; line-height: 1.3; margin-top: 16px; color: var(--ink-soft); font-style: normal; }
  .contact__list { list-style: none; margin-top: 12px; }
  .contact__item {
    display: flex; align-items: center; gap: 12px;
    font-size: 17px; line-height: 1.55; color: var(--ink-soft);
  }
  .contact__icon { width: 16px; height: 16px; flex: none; }
</style>
</head>
<body>
<main class="sheet">

  <section class="card card--front" aria-label="Visitenkarte Vorderseite">
    <span class="brand-name">Wolkenbachtal</span>
    <p class="front__url">www.wolkenbachtal.ch</p>
    <div class="card__band"></div>
  </section>

  <section class="card card--back" aria-label="Visitenkarte Rückseite">
    <span class="brand-name">Wolkenbachtal</span>
    <div class="back__divider"></div>
    <div class="contact">
      <h1 class="contact__name">Dr. Lena Amsler</h1>
      <p class="contact__role">Founder &amp; CEO</p>
      <address class="contact__address">Bachweg 14, 7512<br>Wolkenbach, Switzerland</address>
      <ul class="contact__list">
        <li class="contact__item">
          <svg class="contact__icon" viewBox="0 0 16 16" aria-hidden="true">
            <path d="M4 1.5 L6.2 4.5 L4.8 6 C5.6 7.8 7.6 9.8 10 11 L11.5 9.6 L14.5 11.8 L13 14.5 C7 14 2 9 1.5 3 Z" fill="#fff"/>
          </svg>
          <span>+41 (0) 800 24 60 80</span>
        </li>
        <li class="contact__item">
          <svg class="contact__icon" viewBox="0 0 16 16" aria-hidden="true">
            <rect x="1" y="3" width="14" height="10" fill="#fff"/>
            <path d="M1 3 L8 9 L15 3" fill="none" stroke="#232224" stroke-width="1.3"/>
          </svg>
          <span>hallo@wolkenbachtal.ch</span>
        </li>
        <li class="contact__item">
          <svg class="contact__icon" viewBox="0 0 16 16" aria-hidden="true">
            <circle cx="8" cy="8" r="6.5" fill="none" stroke="#fff" stroke-width="1.3"/>
            <ellipse cx="8" cy="8" rx="2.8" ry="6.5" fill="none" stroke="#fff" stroke-width="1"/>
            <path d="M1.5 8 H14.5 M2.5 5 H13.5 M2.5 11 H13.5" stroke="#fff" stroke-width="1"/>
          </svg>
          <span>www.wolkenbachtal.ch</span>
        </li>
      </ul>
    </div>
    <div class="card__band"></div>
  </section>

</main>
</body>
</html>
```